Landing page for a cyber security service provider called 'Lumen Grove'

The client is a new cyber security company in need of a website landing page at lumengrove.example.

Their visual identity is modern, playful, clean and uncluttered and represents innovation, connectivity and approachability.

The company logo is provided in black (attached) but the client is open to changing the colour to align with the new website design.

The landing page needs to contain:
- A call to action with a 'Get Started' button
-Links to blank 'How it works', 'Products', 'Pricing', 'About Us' and 'Contact Us' pages (that we'll fill out later)

Target Market(s)

Medium to large businesses who probably don't understand cyber / cyber security but need their business to be protected.

Industry/Entity Type

Cyber Security

Coding

Coded - Design and coding required

Number of Pages Required

1 page

Font styles to use
Sans Serif
Other font styles liked:
• Helvetica

Requirements
Nice to have
• Hero banner at the top of the landing page.
Should not have
• Should not look like a traditional cyber / cyber security design (eg no dark blue/ black, red/black colour combinations). Please no military styles (eg no shields, cannons, swords, guns)

```html
<!DOCTYPE html>
<html lang="en">
<head>
<meta charset="utf-8">
<title>Lumen Grove — The Future of Cyber Security</title>
<link href="https://fonts.googleapis.com/css2?family=Audiowide&family=Montserrat:wght@400;500;600;700&display=swap" rel="stylesheet">
<style>
:root{
  --cyan:#7fe4f0;
  --sky:#a9c6f6;
  --pink:#ec6fc6;
  --magenta:#f0418f;
  --purple:#9a6cf1;
  --violet:#7e5bef;
  --lavender:#f4f0fd;
  --ink:#141418;
  --muted:#5b5b66;
  --white:#ffffff;
  --orange:#f0813a;
  --display:"Audiowide",sans-serif;
  --body:"Montserrat",sans-serif;
}
*{box-sizing:border-box;margin:0;padding:0}
html,body{width:1200px;height:4787px;overflow:hidden}
body{position:relative;font-family:var(--body);color:var(--ink);background:var(--white)}
.abs{position:absolute}
a{color:inherit;text-decoration:none}
.label{font-size:13px;color:var(--purple);letter-spacing:.5px;font-weight:500;text-transform:uppercase}
.h2{font-family:var(--display);font-size:40px;line-height:44px;font-weight:400}
.btn-grad{display:flex;align-items:center;justify-content:center;border-radius:30px;background:linear-gradient(90deg,var(--pink),var(--purple));color:var(--white);font-weight:600;font-size:16px;letter-spacing:.5px}
.btn-line{display:flex;align-items:center;justify-content:center;border-radius:30px;border:2px solid var(--pink);color:var(--purple);font-weight:600;font-size:16px;background:var(--white)}

/* hero */
.hero{left:0;top:0;width:1200px;height:600px;background:linear-gradient(115deg,#8ce8f2 0%,#a5d6f5 40%,#c3a4ec 72%,#e87bcb 100%);overflow:hidden}
.hero-wave{left:0;top:380px;width:1200px;height:230px}
.brand{display:flex;align-items:center;gap:10px;color:var(--ink);font-weight:700;font-size:26px}
.brand-dot{width:22px;height:22px;border-radius:50%;background:var(--ink)}
.nav{left:467px;top:52px;display:flex;gap:34px;font-size:13px;font-weight:500;color:#1f2a44;letter-spacing:.3px}
.nav-contact{left:936px;top:38px;width:138px;height:46px;border-radius:24px;background:var(--white);border:2px solid var(--pink);color:var(--pink);font-size:15px;font-weight:500;display:flex;align-items:center;justify-content:center}
.hero-title{left:97px;top:190px;font-family:var(--display);color:var(--white);font-size:58px;line-height:64px}
.hero-sub{left:97px;top:350px;color:var(--white);font-size:22px;line-height:35px;font-weight:500}
.hero-cta{left:97px;top:462px;width:170px;height:42px;font-size:16px}
.hero-art{left:630px;top:90px;width:505px;height:430px;border-radius:30px;background:radial-gradient(circle at 50% 40%,rgba(255,255,255,.75),rgba(190,205,250,.55) 55%,rgba(220,160,235,.25) 80%,transparent)}

/* how */
.how-label{left:0;width:1200px;top:642px;text-align:center}
.how-title{left:0;width:1200px;top:668px;text-align:center}
.how-text{left:270px;width:660px;top:768px;text-align:center;font-size:15px;line-height:23px;color:#333}
.step{width:472px;height:232px;border-radius:22px;overflow:hidden;background:linear-gradient(110deg,#7fe0f0,#a899f0 60%,#b98bef);border-top:8px solid var(--pink)}
.step h3{position:absolute;font-size:25px;font-weight:500;color:var(--white);letter-spacing:1px}
.step p{position:absolute;width:200px;font-size:13px;line-height:20px;color:var(--white)}
.step-panel{position:absolute;top:0;width:236px;height:224px;background:var(--white)}
.step-ph{position:absolute;border-radius:8px}
.how-more{left:514px;top:1422px;width:171px;height:45px}

/* products */
.products{left:0;top:1490px;width:1200px;height:700px;background:linear-gradient(180deg,#fff 0%,var(--lavender) 40%,#f2eefc 100%)}
.prod-label{left:115px;top:1672px}
.prod-title{left:115px;top:1700px}
.prod-text{left:115px;top:1866px;width:380px;font-size:15px;line-height:24px;color:#333}
.prod-btn{left:115px;top:1972px;width:171px;height:45px}
.pcard{width:214px;height:226px;background:var(--white);border-radius:12px;box-shadow:6px 8px 0 -2px var(--pink),0 10px 24px rgba(120,90,200,.12)}
.pcard .pimg{position:absolute;left:22px;top:18px;width:80px;height:90px;border-radius:16px;background:linear-gradient(140deg,#e8d9ff,#b48af3 60%,#e87bd4)}
.pcard h4{position:absolute;left:22px;top:132px;font-size:17px;font-weight:500}
.pcard h4 span{color:var(--orange)}
.pcard p{position:absolute;left:22px;top:158px;width:175px;font-size:13px;line-height:19px;color:#333}

/* pricing */
.price-icon{left:565px;top:2280px;width:70px;height:70px;border-radius:50%;background:linear-gradient(135deg,var(--cyan),var(--pink))}
.price-label{left:0;width:1200px;top:2380px;text-align:center}
.price-title{left:0;width:1200px;top:2408px;text-align:center}
.toggle{left:0;width:1200px;top:2525px;display:flex;justify-content:center;align-items:center;gap:14px;font-size:14px;font-weight:600}
.toggle-track{width:46px;height:24px;border-radius:12px;background:#eee;position:relative}
.toggle-track i{position:absolute;left:2px;top:1px;width:22px;height:22px;border-radius:50%;background:linear-gradient(135deg,var(--cyan),var(--pink))}
.plan{border-radius:16px;background:linear-gradient(180deg,#fdfcff 0%,#e7dcfa 100%);padding:0 37px}
.plan h5{font-size:16px;font-weight:600;margin-top:40px}
.plan .desc{font-size:12px;line-height:16px;margin-top:6px;color:#333}
.plan .price{font-size:34px;font-weight:600;margin-top:28px}
.plan .per{font-size:12px;margin-top:4px;color:#333}
.plan ul{list-style:none;margin-top:44px;font-size:12px;line-height:23.5px}
.plan li{display:flex;align-items:center;gap:8px}
.plan li svg{flex:none}
.plan .btn-grad{position:absolute;left:31px;right:31px;bottom:36px;height:42px}
.plan-pro{background:linear-gradient(180deg,#9a6df0 0%,#b46ae6 60%,#d06fdd 100%);color:var(--white)}
.plan-pro .desc,.plan-pro .per{color:#f0e7ff}
.plan-pro hr{border:0;border-top:1px solid rgba(255,255,255,.6);margin-top:10px}
.plan-pro .btn-pro{position:absolute;left:31px;right:31px;bottom:28px;height:44px;border-radius:24px;background:linear-gradient(90deg,#fff,#d6f6fb);color:#6b8bd8;display:flex;align-items:center;justify-content:center;font-weight:600;font-size:16px}

/* about */
.laptop{left:0;top:3216px;width:545px;height:420px;border-radius:0 18px 18px 0;background:linear-gradient(160deg,#f6f5fb,#e2e6f4 70%,#c9cbd8);border:10px solid #1c1c22;border-left:0}
.about-label{left:641px;top:3226px}
.about-title{left:636px;top:3256px}
.about-text{left:636px;top:3324px;width:440px;font-size:15px;line-height:23px;color:#333}
.feat{width:210px}
.feat-head{display:flex;align-items:center;gap:12px;font-size:15px;font-weight:600;color:#3c2fa0;line-height:19px}
.feat-icon{width:38px;height:38px;border-radius:6px;background:linear-gradient(135deg,var(--violet),var(--pink));flex:none}
.feat p{margin-top:16px;font-size:14px;line-height:24px;color:#333}

/* contact */
.contact{left:0;top:3650px;width:1200px;height:1137px}
.contact-label{left:0;width:1200px;top:3752px;text-align:center;color:#6b79d8}
.contact-title{left:0;width:1200px;top:3782px;text-align:center;color:var(--white)}
.contact-text{left:330px;width:540px;top:3900px;text-align:center;color:var(--white);font-size:15px;line-height:24px;font-weight:500}
.form{left:214px;top:3980px;width:772px;height:404px;border-radius:22px;background:var(--white);box-shadow:12px 14px 0 rgba(70,60,160,.45)}
.field{position:absolute}
.field label{display:block;font-size:15px;font-weight:600;margin-bottom:6px}
.field .box{height:46px;border:1.5px solid #d9d9de;border-radius:8px;padding:0 18px;display:flex;align-items:center;justify-content:space-between;font-size:13px;color:#9a9aa3}
.submit{left:514px;top:4323px;width:171px;height:44px}

/* footer */
.foot-brand{left:126px;top:4600px;color:var(--white);font-size:30px}
.foot-brand .brand-dot{background:var(--white)}
.socials{left:138px;top:4685px;display:flex;gap:14px}
.socials i{width:20px;height:20px;border-radius:4px;background:var(--white)}
.fcol{top:4548px;padding-left:16px;border-left:2px solid var(--white);color:var(--white)}
.fcol h6{font-size:15px;font-weight:600;margin-bottom:14px;color:#ffe9f6}
.fcol a{display:block;font-size:13px;line-height:25px}
.fcol .row{display:flex;gap:10px;font-size:13px;line-height:19px;margin-bottom:10px}
.totop{left:1088px;top:4668px;width:54px;height:54px;border-radius:50%;background:linear-gradient(135deg,#3e9af5,#6fc3f5);border:3px solid var(--white);display:flex;align-items:center;justify-content:center}
.copy{left:0;width:1200px;top:4740px;text-align:center;color:var(--white);font-size:12px}
</style>
</head>
<body>

<!-- HERO -->
<section class="abs hero">
  <div class="abs hero-art" role="img" aria-label="Illustration of a laptop surrounded by floating security dashboards and profile cards"></div>
  <svg class="abs hero-wave" viewBox="0 0 1200 230" preserveAspectRatio="none"><path d="M0 190 C200 230 360 200 470 120 C560 50 640 40 730 110 C840 190 980 210 1200 200 L1200 230 L0 230Z" fill="#fff"/></svg>
</section>
<a class="abs brand" style="left:117px;top:64px"><span class="brand-dot"></span>Lumen Grove</a>
<nav class="abs nav"><a>HOW IT WORKS</a><a>PRODUCTS</a><a>PRICING</a><a>ABOUT US</a></nav>
<a class="abs nav-contact">Contact Us</a>
<h1 class="abs hero-title">The Future of<br>Cyber Security</h1>
<p class="abs hero-sub">Modern Solutions for Comprehensive<br>Protection and Peace of Mind</p>
<a class="abs btn-grad hero-cta">GET STARTED</a>

<!-- HOW IT WORKS -->
<p class="abs label how-label">How it works</p>
<h2 class="abs h2 how-title">How We Protect Your<br>Organization</h2>
<p class="abs how-text">At Lumen Grove, we believe in a seamless approach to cybersecurity. Our platform is designed to provide you with comprehensive protection through a series of easy-to-follow steps. Here's how Lumen Grove keeps you secure</p>

<div class="abs step" style="left:115px;top:882px">
  <h3 style="left:30px;top:55px">PREVENT</h3>
  <p style="left:30px;top:100px">Detect vulnerabilities and block threats before they occur.</p>
  <div class="step-panel" style="right:0">
    <svg width="236" height="224" viewBox="0 0 236 224" font-family="Montserrat" font-size="8" fill="#555">
      <text x="20" y="40" font-size="9" fill="#222">Statistics</text>
      <circle cx="150" cy="37" r="2.5" fill="#f0418f"/><text x="156" y="40">High Risk</text>
      <circle cx="150" cy="49" r="2.5" fill="#3b5bdb"/><text x="156" y="52">Low Risk</text>
      <g stroke="#eee"><line x1="35" y1="80" x2="220" y2="80"/><line x1="35" y1="110" x2="220" y2="110"/><line x1="35" y1="140" x2="220" y2="140"/><line x1="35" y1="170" x2="220" y2="170"/></g>
      <path d="M40 165 C60 150 70 120 90 150 C110 180 125 110 145 120 C165 130 175 90 190 110 C200 120 210 80 218 70" fill="none" stroke="#3b5bdb" stroke-width="2"/>
      <path d="M40 170 C60 170 80 140 100 130 C120 120 130 160 150 140 C170 120 185 150 200 110 C208 95 214 90 218 90" fill="none" stroke="#f0418f" stroke-width="2"/>
      <text x="45" y="190">Jul</text><text x="95" y="190">Aug</text><text x="145" y="190">Sep</text><text x="195" y="190">Oct</text>
    </svg>
  </div>
</div>

<div class="abs step" style="left:613px;top:882px">
  <h3 style="left:38px;top:55px">PROTECT</h3>
  <p style="left:38px;top:100px">Safeguard your data with advanced encryption and security measures.</p>
  <div class="step-panel" style="right:0">
    <svg width="236" height="224" viewBox="0 0 236 224" font-family="Montserrat" font-size="7" fill="#333">
      <text x="118" y="22" text-anchor="middle" font-size="8">Protection Effectiveness</text>
      <circle cx="118" cy="72" r="26" fill="none" stroke="#f7d9c6" stroke-width="9"/>
      <circle cx="118" cy="72" r="26" fill="none" stroke="#f0813a" stroke-width="9" stroke-dasharray="130 200" transform="rotate(-90 118 72)"/>
      <circle cx="118" cy="72" r="14" fill="none" stroke="#3b5bdb" stroke-width="5" stroke-dasharray="70 100"/>
      <rect x="14" y="128" width="208" height="12" fill="#f3f3f6"/>
      <circle cx="18" cy="155" r="2" fill="#3b5bdb"/><text x="24" y="158">Threats Blocked</text><text x="200" y="158" fill="#2bb673">82%</text>
      <circle cx="18" cy="173" r="2" fill="#3b5bdb"/><text x="24" y="176">Encryption Rate</text><text x="200" y="176" fill="#2bb673">99%</text>
      <circle cx="18" cy="191" r="2" fill="#3b5bdb"/><text x="24" y="194">Secure Links</text><text x="200" y="194" fill="#2bb673">98%</text>
    </svg>
  </div>
</div>

<div class="abs step" style="left:115px;top:1138px">
  <div class="step-panel" style="left:0;background:#fff">
    <div class="step-ph" style="left:14px;top:18px;width:210px;height:190px;background:linear-gradient(135deg,#e6f0ff,#f5e6fb)" role="img" aria-label="Workflow diagram of task tags linked to a completed-task chart"></div>
  </div>
  <h3 style="left:270px;top:55px">RESPOND</h3>
  <p style="left:270px;top:100px">Quickly neutralize detected threats with automated responses.</p>
</div>

<div class="abs step" style="left:613px;top:1138px">
  <div class="step-panel" style="left:0;background:#fff">
    <div class="step-ph" style="left:10px;top:24px;width:216px;height:180px;background:linear-gradient(135deg,#dfe8fb,#c9d6f5)" role="img" aria-label="World map of user locations with country statistics"></div>
  </div>
  <h3 style="left:270px;top:55px">MONITOR</h3>
  <p style="left:270px;top:100px">Ensure continuous protection with real-time monitoring and updates.</p>
</div>

<a class="abs btn-line how-more">LEARN MORE</a>

<!-- PRODUCTS -->
<section class="abs products"></section>
<p class="abs label prod-label">Products</p>
<h2 class="abs h2 prod-title">Explore Our<br>Cybersecurity<br>Products</h2>
<p class="abs prod-text">Discover Lumen Grove's innovative solutions designed to protect your digital environment with cutting-edge technology and user-friendly features.</p>
<a class="abs btn-grad prod-btn">LEARN MORE</a>

<div class="abs pcard" style="left:604px;top:1603px"><div class="pimg" role="img" aria-label="3D shield-free abstract shape"></div><h4><span>Lumen</span>Shield</h4><p>Real-time antivirus and malware protection.</p></div>
<div class="abs pcard" style="left:845px;top:1643px"><div class="pimg" role="img" aria-label="3D diamond shape"></div><h4><span>Lumen</span>Guard</h4><p>Advanced firewall for network security.</p></div>
<div class="abs pcard" style="left:604px;top:1835px"><div class="pimg" role="img" aria-label="3D bar shapes"></div><h4><span>Lumen</span>Secure</h4><p>Data encryption to protect your information.</p></div>
<div class="abs pcard" style="left:845px;top:1878px"><div class="pimg" role="img" aria-label="3D ring shape"></div><h4><span>Lumen</span>Monitor</h4><p>24/7 system monitoring with instant alerts.</p></div>

<!-- PRICING -->
<div class="abs price-icon"></div>
<p class="abs label price-label">Pricing</p>
<h2 class="abs h2 price-title">Choose the Right Plan<br>for Your Needs</h2>
<div class="abs toggle"><span>Pay Monthly</span><span class="toggle-track"><i></i></span><span>Pay Earthly</span></div>

<div class="abs plan" style="left:115px;top:2615px;width:307px;height:421px">
  <h5>Basic</h5><p class="desc">Essential antivirus and firewall.</p>
  <p class="price">$59.99</p><p class="per">Per user month</p>
  <ul>
    <li><svg width="12" height="10"><path d="M1 5l3.5 3.5L11 1" stroke="#2bb673" stroke-width="2" fill="none"/></svg>Essential antivirus</li>
    <li><svg width="12" height="10"><path d="M1 5l3.5 3.5L11 1" stroke="#2bb673" stroke-width="2" fill="none"/></svg>Basic firewall protection</li>
    <li><svg width="12" height="10"><path d="M1 5l3.5 3.5L11 1" stroke="#2bb673" stroke-width="2" fill="none"/></svg>Standard encryption</li>
    <li><svg width="12" height="10"><path d="M1 5l3.5 3.5L11 1" stroke="#2bb673" stroke-width="2" fill="none"/></svg>Easy setup</li>
    <li><svg width="12" height="10"><path d="M1 5l3.5 3.5L11 1" stroke="#2bb673" stroke-width="2" fill="none"/></svg>Affordable</li>
  </ul>
  <a class="btn-grad">GET STARTED</a>
</div>

<div class="abs plan plan-pro" style="left:446px;top:2585px;width:306px;height:479px">
  <h5>Professional</h5><p class="desc">Advanced firewall and 24/7 monitoring.</p>
  <p class="price">$89.99</p><p class="per">Per user month</p><hr>
  <ul>
    <li><svg width="12" height="10"><path d="M1 5l3.5 3.5L11 1" stroke="#fff" stroke-width="2" fill="none"/></svg>Advanced firewall</li>
    <li><svg width="12" height="10"><path d="M1 5l3.5 3.5L11 1" stroke="#fff" stroke-width="2" fill="none"/></svg>Enhanced data encryption</li>
    <li><svg width="12" height="10"><path d="M1 5l3.5 3.5L11 1" stroke="#fff" stroke-width="2" fill="none"/></svg>24/7 system monitoring</li>
    <li><svg width="12" height="10"><path d="M1 5l3.5 3.5L11 1" stroke="#fff" stroke-width="2" fill="none"/></svg>Detailed threat reports</li>
    <li><svg width="12" height="10"><path d="M1 5l3.5 3.5L11 1" stroke="#fff" stroke-width="2" fill="none"/></svg>Scalable for growth</li>
  </ul>
  <a class="btn-pro">GET STARTED</a>
</div>

<div class="abs plan" style="left:778px;top:2615px;width:306px;height:421px">
  <h5 style="margin-top:32px">Enterprise</h5><p class="desc">Custom security and dedicated support.</p>
  <p class="price" style="margin-top:20px">$99.99</p><p class="per">Per user month</p>
  <ul>
    <li><svg width="12" height="10"><path d="M1 5l3.5 3.5L11 1" stroke="#2bb673" stroke-width="2" fill="none"/></svg>Customizable security solutions</li>
    <li><svg width="12" height="10"><path d="M1 5l3.5 3.5L11 1" stroke="#2bb673" stroke-width="2" fill="none"/></svg>Advanced threat detection</li>
    <li><svg width="12" height="10"><path d="M1 5l3.5 3.5L11 1" stroke="#2bb673" stroke-width="2" fill="none"/></svg>Dedicated support team</li>
    <li><svg width="12" height="10"><path d="M1 5l3.5 3.5L11 1" stroke="#2bb673" stroke-width="2" fill="none"/></svg>Comprehensive coverage</li>
    <li><svg width="12" height="10"><path d="M1 5l3.5 3.5L11 1" stroke="#2bb673" stroke-width="2" fill="none"/></svg>Tailored for large organizations</li>
  </ul>
  <a class="btn-grad">GET STARTED</a>
</div>

<!-- ABOUT -->
<div class="abs laptop" role="img" aria-label="Laptop screen showing a user behaviour analytics dashboard"></div>
<p class="abs label about-label">About us</p>
<h2 class="abs h2 about-title">Who We Are</h2>
<p class="abs about-text">At Lumen Grove, we're dedicated to revolutionizing cybersecurity with innovative, user-friendly solutions. Our mission is to provide effective protection that's easy to manage, so you can focus on what matters most.</p>
<div class="abs feat" style="left:636px;top:3454px"><div class="feat-head"><span class="feat-icon"></span>Cutting-Edge<br>Technology</div><p>We leverage the latest advancements to keep you secure.</p></div>
<div class="abs feat" style="left:877px;top:3454px"><div class="feat-head"><span class="feat-icon"></span>Customer-Centric<br>Approach</div><p>We leverage the latest advancements to keep you secure.</p></div>

<!-- CONTACT + FOOTER BACKGROUND -->
<svg class="abs contact" viewBox="0 0 1200 1137" preserveAspectRatio="none">
  <defs>
    <linearGradient id="contactBg" x1="0" y1="0" x2="0.35" y2="1">
      <stop offset="0" stop-color="#86e6f0"/>
      <stop offset=".35" stop-color="#a9b8f2"/>
      <stop offset=".6" stop-color="#d97bd0"/>
      <stop offset=".8" stop-color="#b34fb8"/>
      <stop offset="1" stop-color="#ef3f8f"/>
    </linearGradient>
  </defs>
  <path d="M0 50 C150 0 300 20 450 55 C620 95 760 40 900 30 C1030 22 1120 40 1200 60 L1200 1137 L0 1137Z" fill="url(#contactBg)"/>
</svg>
<p class="abs label contact-label">Contact us</p>
<h2 class="abs h2 contact-title">Let's Protect Your<br>Organization</h2>
<p class="abs contact-text">Use this form to ask a question and send us a comment &amp; we will respond within 1 business day!</p>

<form class="abs form">
  <div class="field" style="left:34px;top:32px;width:340px"><label>Full Name</label><div class="box">Enter your name<svg width="12" height="12"><circle cx="6" cy="4" r="3" fill="#bbb"/><path d="M0 12c0-4 12-4 12 0z" fill="#bbb"/></svg></div></div>
  <div class="field" style="left:396px;top:32px;width:342px"><label>Phono No</label><div class="box">555 014 2297<svg width="12" height="12"><path d="M2 1l3 0 1 3-2 1c1 2 2 3 4 4l1-2 3 1 0 3c-6 0-10-4-10-10z" fill="#bbb"/></svg></div></div>
  <div class="field" style="left:34px;top:108px;width:704px"><label>Email Address</label><div class="box">info@lumengrove.example<svg width="13" height="10"><rect x=".5" y=".5" width="12" height="9" fill="none" stroke="#bbb"/><path d="M1 1l5.5 5L12 1" fill="none" stroke="#bbb"/></svg></div></div>
  <div class="field" style="left:34px;top:184px;width:704px"><label>Message</label><div class="box" style="height:120px;align-items:flex-start;padding-top:14px">Type your message here<svg width="12" height="12"><circle cx="6" cy="6" r="5.5" fill="#ccc"/></svg></div></div>
</form>
<a class="abs btn-grad submit">SUBMIT NOW</a>

<div class="abs brand foot-brand"><span class="brand-dot"></span>Lumen Grove</div>
<div class="abs socials"><i></i><i></i><i></i></div>

<div class="abs fcol" style="left:409px">
  <h6>Quick Links</h6><a>How it works</a><a>Products</a><a>Pricing</a><a>About Us</a>
</div>
<div class="abs fcol" style="left:622px">
  <h6>Security</h6><a>LumenShield</a><a>LumenGuard</a><a>LumenSecure</a><a>LumenMonitor</a>
</div>
<div class="abs fcol" style="left:817px;width:240px">
  <h6>Contact Info</h6>
  <div class="row"><svg width="12" height="16" style="flex:none"><path d="M6 0a6 6 0 0 1 6 6c0 4-6 10-6 10S0 10 0 6a6 6 0 0 1 6-6z" fill="#fff"/><circle cx="6" cy="6" r="2.2" fill="#c552b5"/></svg>48 Fernleaf Row, Alder Bay,<br>Oregon 90417</div>
  <div class="row"><svg width="14" height="14" style="flex:none"><path d="M2 1l3 0 1 3-2 1c1 2 3 4 5 5l1-2 3 1 0 3C6 13 1 8 2 1z" fill="#fff"/></svg>555-014-2297</div>
  <div class="row"><svg width="14" height="11" style="flex:none"><rect width="14" height="11" rx="1" fill="#fff"/><path d="M1 1l6 5 6-5" fill="none" stroke="#d4489f"/></svg>hello@lumengrove.example</div>
</div>

<a class="abs totop"><svg width="22" height="24"><path d="M11 22V3M3 11l8-8 8 8" fill="none" stroke="#fff" stroke-width="2.5" stroke-linecap="round"/></svg></a>
<p class="abs copy">Lumen Grove © 2024 All rights reserved.</p>

</body>
</html>
```